Vocational Mentor needs an impressive business card

1. I need a business card (or maybe three with identic look) to promote me and my three business titles/services:
- Vocational Mentor. I help people find their vocation and live happily from it. I use my 20 years of experience in business, management and psychology to help them identify the most efficient ways to make a living doing what they are passionate about.
- Business Angel. I help founders start a succesful business with minimum risks and costs. I use my 20 years of experience in sales, management and entrepreneurship to help them identify the most efficient ways, in terms of time and cost, to validate their business idea.
- Learning Designer. I design unique learning programs that produce long-term cognitive and behavioural changes to people and organisations. I use my 20 years of experience in learning, teaching and change management to create minimalist experiences and processes that allow them to change efficiently in their pursued direction.

2. I would like a two-sided business card, on the front with my name, contact details and titles, on the back the explanation of the services.
Updates

Hi all,

I updated my brief, included contacts info and give feedback on all designs I got. I am new on this platform so please tell me if you need anything else or if I don't use corectly the platform forms.

Kind regards,
Tudor

Hi all,

I shortened the services description by deleting the phrase "I call..."

Kind regards,
Tudor

Target Market(s)

Freelancers, startups, people and organization willing to invest in change through ultimate learning experiences

Industry/Entity Type

Business

Font styles to use
Serif

Requirements
Must have
• Front side: full name, titles, web site, email, phone like below:
Tudor Vasilache
Vocational Mentor, Business Angel, Learning Designer
info@tudorvasilache.example
www.tudorvasilache.example
+40-745-TUDORV
Nice to have
• Back side: the description of the services I provide as in the task description.
1/3: it would be nice if I can jam all three titles on the front side but then I need a solution to jam all three services on the back side.

```html
<!DOCTYPE html>
<html lang="en">
<head>
<meta charset="utf-8">
<title>Tudor Vasilache – Business Card</title>
<link rel="stylesheet" href="https://fonts.googleapis.com/css2?family=Oswald:wght@300;400&family=Questrial&display=swap">
<style>
  :root {
    --canvas-bg: #d9d9d9;
    --card-white: #ffffff;
    --card-dark: #5d5d5d;
    --brand-blue: #2f6db5;
    --text-grey: #555555;
    --text-light: #ffffff;
    --card-shadow: 0 6px 18px rgba(0, 0, 0, 0.18);
  }

  * { box-sizing: border-box; margin: 0; padding: 0; }

  html, body {
    width: 1200px;
    height: 1000px;
    overflow: hidden;
  }

  body {
    background: var(--canvas-bg);
    position: relative;
    font-family: "Questrial", Arial, sans-serif;
  }

  .card {
    position: absolute;
    left: 220px;
    width: 760px;
    height: 434px;
    box-shadow: var(--card-shadow);
    overflow: hidden;
  }

  /* Back side */
  .card--back {
    top: 50px;
    background: var(--card-dark);
  }

  .back-marker {
    position: absolute;
    left: 28px;
    top: 28px;
    width: 34px;
    height: 34px;
    background: var(--brand-blue);
  }

  .back-marker svg {
    display: block;
    width: 34px;
    height: 34px;
  }

  .service-text {
    position: absolute;
    left: 78px;
    top: 26px;
    width: 440px;
    color: var(--text-light);
    font-size: 15px;
    line-height: 1.35;
    letter-spacing: 0.2px;
  }

  /* Front side */
  .card--front {
    top: 516px;
    background: var(--card-white);
  }

  .name-band {
    position: absolute;
    left: 372px;
    right: 0;
    top: 92px;
    height: 46px;
    background: var(--brand-blue);
    display: flex;
    align-items: center;
    padding-left: 20px;
  }

  .name {
    font-family: "Oswald", "Arial Narrow", sans-serif;
    font-weight: 300;
    font-size: 27px;
    letter-spacing: 3px;
    text-transform: uppercase;
    color: var(--text-light);
    white-space: nowrap;
  }

  .title {
    position: absolute;
    right: 46px;
    top: 146px;
    font-size: 19px;
    color: var(--brand-blue);
    letter-spacing: 0.3px;
  }

  .contact-list {
    position: absolute;
    right: 46px;
    top: 212px;
    list-style: none;
    text-align: right;
    color: var(--text-grey);
    font-size: 19px;
    line-height: 30px;
    letter-spacing: 0.2px;
  }
</style>
</head>
<body>

  <section class="card card--back" aria-label="Business card, back side">
    <div class="back-marker">
      <svg viewBox="0 0 34 34" aria-hidden="true">
        <polyline points="13,9 21,17 13,25" fill="none" stroke="#ffffff" stroke-width="4" stroke-linecap="square"/>
      </svg>
    </div>
    <p class="service-text">I help people to find their vocation and live happily from it. I use my 20 years of experience in business, management and psychology to help them identify the most efficient ways to make a living doing what they are passionate about.</p>
  </section>

  <section class="card card--front" aria-label="Business card, front side">
    <div class="name-band">
      <h1 class="name">Tudor Vasilache</h1>
    </div>
    <p class="title">vocational mentor</p>
    <ul class="contact-list">
      <li class="contact-email">info@tudorvasilache.example</li>
      <li class="contact-web">www.tudorvasilache.example</li>
      <li class="contact-phone">+40-745-TUDORV</li>
    </ul>
  </section>

</body>
</html>
```